Book cover needed for self help business book

Book cover needed and I will provide back cover blurb and barcode to the winning designer. Book may be too small for spine, but I will give you the page number details to confirm. Book information below:

Title: Nine Winters a Trader
Subtitle: Proven Market Methods That Keep Paying Off Now
Author: Maribel Okonte

Design should be clean, modern, and bold—something that appeals to everyday entrepreneurs and resellers. The cover should reflect grit, real-world hustle, and long-term wisdom without looking overly corporate or flashy. I am open to your creative ideas.

I am open to modern designs, but also designs of rugged old covers that simulate a book that may have aged over the years.

I prefer not to have pictures or silhouettes of people

Requirements
Nice to have
• I am open to modern designs, but also designs of rugged old covers that simulate a book that may have aged over the years.
Should not have
• Pictures or silhouettes of people

```html
<!DOCTYPE html>
<html lang="en">
<head>
<meta charset="utf-8">
<title>Nine Winters a Trader — Book Cover</title>
<link rel="stylesheet" href="https://fonts.googleapis.com/css2?family=Barlow+Condensed:wght@600;700&family=Montserrat:wght@700&display=swap">
<style>
  :root {
    --cover-navy: #002b63;
    --title-yellow: #ffe500;
    --ink-white: #ffffff;
    --band-red: #b80000;
  }
  html, body {
    margin: 0;
    padding: 0;
    width: 800px;
    height: 1200px;
    overflow: hidden;
    background: var(--cover-navy);
  }
  .book-cover {
    display: block;
    width: 800px;
    height: 1200px;
  }
  .cover-ground { fill: var(--cover-navy); }
  .author-band { fill: var(--band-red); }
  .title-display {
    font-family: "Barlow Condensed", "Arial Narrow", sans-serif;
    font-weight: 700;
  }
  .title-yellow { fill: var(--title-yellow); }
  .title-white { fill: var(--ink-white); }
  .title-rule { fill: var(--ink-white); }
  .subtitle-line {
    font-family: "Montserrat", Arial, sans-serif;
    font-weight: 700;
    font-size: 24px;
    fill: var(--ink-white);
  }
  .author-name {
    font-family: "Montserrat", Arial, sans-serif;
    font-weight: 700;
    font-size: 44px;
    fill: var(--ink-white);
  }
</style>
</head>
<body>
<svg class="book-cover" viewBox="0 0 800 1200" xmlns="http://www.w3.org/2000/svg" role="img" aria-label="Nine Winters a Trader: Proven Market Methods That Keep Paying Off Now, by Maribel Okonte">
  <rect class="cover-ground" x="0" y="0" width="800" height="1200"/>

  <g class="title-block">
    <text class="title-display title-yellow title-line-first" x="400" y="480" text-anchor="middle" font-size="611" textLength="520" lengthAdjust="spacingAndGlyphs">NINE</text>
    <text class="title-display title-yellow title-line-second" x="400" y="671" text-anchor="middle" font-size="234" textLength="520" lengthAdjust="spacingAndGlyphs">WINTERS</text>

    <rect class="title-rule" x="53" y="716" width="318" height="4"/>
    <rect class="title-rule" x="428" y="716" width="318" height="4"/>
    <text class="title-display title-white title-connector" x="400" y="748" text-anchor="middle" font-size="83">A</text>

    <text class="title-display title-white title-line-last" x="400" y="960" text-anchor="middle" font-size="257" textLength="692" lengthAdjust="spacingAndGlyphs">TRADER</text>
  </g>

  <g class="subtitle-block">
    <text class="subtitle-line" x="400" y="1044" text-anchor="middle">PROVEN MARKET METHODS THAT</text>
    <text class="subtitle-line" x="400" y="1078" text-anchor="middle">KEEP PAYING OFF NOW</text>
  </g>

  <rect class="author-band" x="0" y="1121" width="800" height="79"/>
  <text class="author-name" x="400" y="1177" text-anchor="middle" textLength="560" lengthAdjust="spacing">MARIBEL OKONTE</text>
</svg>
</body>
</html>
```